Manufacturing company needs new business card.

I need a unique Business Card that will truly stand out. Nothing too busy. Simple is good, right? Not looking for a standard design either. No cookie cutter layout. I am just looking for something interesting and a bit different. Does't have to completely off the wall crazy, just not your run of the mill business card. Clean and modern with a touch of industrial.

Target Market(s)

Air conditioning industry, Architects, builders.

Industry/Entity Type

Business

Contact Information for Business Card

Details to be included on card are:

Peter Vance
Managing Director

T: 1300 847 519
M: 0428 593 174
W: www.brenvaleworks.com.au
E: peter.vance@brenvaleworks.com.au
A: 58 Harwick Lane, Sydney NSW 2000

Font styles to use
Sans Serif

Colors
0355a3
848484
fbfbfb

Requirements
Must have
• Card design must be landscape.

```html
<!DOCTYPE html>
<html lang="en">
<head>
<meta charset="utf-8">
<title>Brenvale Works – Business Card</title>
<link href="https://fonts.googleapis.com/css2?family=Pathway+Gothic+One&display=swap" rel="stylesheet">
<style>
  :root {
    --page: #ffffff;
    --card: #000000;
    --ink: #fbfbfb;
    --brand: #3a57a4;
    --shade: #232323;
  }
  * { margin: 0; padding: 0; box-sizing: border-box; }
  html, body {
    width: 1200px;
    height: 1000px;
    overflow: hidden;
    background: var(--page);
  }
  .card {
    position: absolute;
    left: 270px;
    top: 311px;
    width: 660px;
    height: 378px;
    background: var(--card);
    color: var(--ink);
    font-family: "Pathway Gothic One", "Arial Narrow", sans-serif;
    overflow: hidden;
  }
  .backdrop-block {
    position: absolute;
    left: 416px;
    top: 88px;
    width: 204px;
    height: 204px;
    border-radius: 14px;
    background: var(--shade);
  }
  .person {
    position: absolute;
    left: 39px;
    top: 21px;
    font-size: 17px;
    line-height: 19px;
  }
  .phones {
    position: absolute;
    right: 45px;
    top: 27px;
    text-align: right;
    font-size: 15px;
    line-height: 16px;
    letter-spacing: 0.3px;
  }
  .brand {
    position: absolute;
    left: 121px;
    top: 169px;
    display: flex;
    align-items: center;
    gap: 30px;
  }
  .brand-square {
    width: 63px;
    height: 63px;
    border-radius: 4px;
    background: var(--brand);
  }
  .brand-name {
    color: var(--brand);
    font-size: 46px;
    line-height: 1;
    letter-spacing: 1px;
    white-space: nowrap;
  }
  .contact-line {
    position: absolute;
    left: 0;
    right: 0;
    top: 324px;
    text-align: center;
    font-size: 15px;
    word-spacing: 1px;
    white-space: nowrap;
  }
  .contact-line span + span { margin-left: 14px; }
</style>
</head>
<body>
  <section class="card">
    <div class="backdrop-block"></div>

    <div class="person">
      <p class="person-name">Peter Vance</p>
      <p class="person-title">Managing Director</p>
    </div>

    <div class="phones">
      <p>T: 1300 847 519</p>
      <p>M: 0428 593 174</p>
    </div>

    <div class="brand">
      <div class="brand-square"></div>
      <p class="brand-name">Brenvale Works Australia</p>
    </div>

    <p class="contact-line">
      <span>W: www.brenvaleworks.com.au</span>
      <span>E: peter.vance@brenvaleworks.com.au</span>
      <span>A: 58 Harwick Lane, Sydney NSW 2000</span>
    </p>
  </section>
</body>
</html>
```